Design flat ui arx 3 inspired app

Know how you fit in the family and how you relate as a family through a shared Tree.
· Keep track of your family as it expands
· Merge family trees or join a common family Tree
· Share family moments by uploading pictures and videos on your calendar
· Get notifications of all events, additions, and other changes to the family tree
· Know where everyone is by keeping in touch through real-time chats
· Share your Tree with friends on social media
· Search for long lost family members and friends
· A great way for your kids to know where they come from

Providing a mobile app that allows users to not only create their family trees but allow them to invite other family members to participate in the completion of the family tree. • User downloads and installs the mobile app, then they proceed to signing up • Signing up the user should provide the following information; profile picture, first name, last name, date of birth, gender, password, email address, country, current city, mobile number • The next step is verifying the mobile number by asking the user to enter the six digit number that was sent to them via sms • Once the mobile number is verified your next step is to enter your family, start with you parents, then spouse(s) or partner(s), then siblings and children if any. This step should be optional, meaning users can skip this step • The app should have a menu bar at the bottom(action bar) with fiver menu items namely, Home, Edit, Tree, Stats, Calendar. • After the user has been signed in their first experience is the home screen, with the profile picture displayed, along with the user’s first name, last name, and age(all the above should be static). Just below all this are three tabs for notifications, photos, and birthdays. • The notifications tab will list all notifications one after the other in text form, example; Kevin updated his high school, Nora added a new member, Brenda has a graduation party coming up, Gordon updated his work experience, Hilda updated her maiden name, Esther updated her siblings, Milton updated his children etc. • Photo’s tab will list all pictures uploaded sorted by latest pictures uploaded and tagged in. One should be able to scroll through the pictures and then when they click on one they can slide though them one after the next viewing them. One should be able to go back to the home screen by clicking the back button. There should be an option to add more photos and share the current ones. • The last tab should be birthdays, which simply lists all birthdays of people who have been entered into the tree from parents to spouses to siblings to children. The birthdays should be listed sorted by month then day, and you should be able to see how old the person is turning. • The next menu bar is the Edit menu which has three tabs namely personal details, family and advanced details. Personal details will have the profile picture, first name, second name, last name, date of birth, gender, twin(if twin then state), relationship status(list spouse if not single), city or place of birth, and living or not. The next tab is the family tab which list and allows you to edit parents, spouse, siblings, and children. The last tab is advanced details, which is hobbies, languages, education, and work experience. • Then the most important part of the app is the Tree function which displays the users family tree, this is all the people added so far and each person is represented by a square with smooth edges, first name and last name displayed first, then age with a green button showing online and a red one showing offline, and below a profile picture. All the relations showed by a line joining the related people. If the person has many spouses they should be stacked together and kids don’t have to show which parent us theirs. One should be able to edit a profile, view a profile, view stats, invite and share. When you invite that person an sms should be generated and the user can enter the mobile number of the family member and once the family members accepts the invitation they then are a member of the tree who can receive notifications on any changes on the tree. Anyone should be able to invite anyone and everyone should see all notifications from everyone who is a member. • The next menu is the statistics menu which displays gender stats, age distribution, birthdays, relationship status, zodiac signs, living vs not living • The last one is the calendar menu which has a calendar where people can add events, upload media, and when a day is clicked and has events on, they should show at the bottom one after the other.

```html
<!DOCTYPE html>
<html lang="en">
<head>
<meta charset="utf-8">
<title>KINROOT – family tree app screens</title>
<link rel="stylesheet" href="https://fonts.googleapis.com/css2?family=Source+Sans+3:wght@400;600;700&display=swap">
<style>
:root{
  --canvas:#27313b;
  --green:#7bd43f;
  --green-dark:#6cc233;
  --green-bright:#9ef05c;
  --green-text:#5cb82a;
  --panel-dark:#3a3a38;
  --field:#efefef;
  --field-line:#dcdcdc;
  --ink:#333;
  --muted:#7a7a7a;
  --white:#fff;
  --photo-warm-1:#8a7a6e;
  --photo-warm-2:#5b5550;
}
*{box-sizing:border-box;margin:0;padding:0}
html,body{width:940px;height:1200px;overflow:hidden;background:var(--canvas)}
body{font-family:"Source Sans 3",sans-serif;color:var(--ink)}
.stage{position:relative;width:1018px;height:1300px;transform:scale(.92338);transform-origin:0 0}
.screen{position:absolute;width:232px;overflow:hidden;background:var(--white)}
.status{position:relative;height:17px;display:flex;align-items:center;justify-content:space-between;padding:0 7px;font-size:9px;color:var(--white);z-index:2}
.status .carrier{display:flex;align-items:center;gap:3px}
.status .time{position:absolute;left:0;right:0;text-align:center;pointer-events:none}
.status .batt{display:flex;align-items:center;gap:3px}
.status.dim{background:rgba(40,40,40,.35)}
.status.green{background:var(--green-dark)}
.appbar{height:44px;background:var(--green);display:flex;align-items:center;justify-content:space-between;padding:0 12px;color:var(--white)}
.appbar h1{font-size:14px;font-weight:600;letter-spacing:.2px}
.pill{height:21px;border-radius:11px;background:var(--field);border:1px solid var(--field-line);font-size:8.5px;color:var(--muted);display:flex;align-items:center;padding:0 10px;text-transform:uppercase}
.select{justify-content:space-between}
.select::after{content:"";border:3px solid transparent;border-top:4px solid var(--green);margin-top:4px}
.label{font-size:9px;font-weight:700;text-transform:uppercase;color:var(--ink);letter-spacing:.2px}
.btn{border-radius:16px;background:var(--green-bright);display:flex;align-items:center;justify-content:center;font-size:12.5px;color:#1e3a0c;text-transform:uppercase}
.brandmark{display:flex;align-items:center;justify-content:center;gap:7px;color:var(--green-bright);font-weight:700}
.brandmark i{display:block;border-radius:50%;background:var(--green-bright)}

/* splash */
.splash{left:73px;top:67px;height:348px;background:linear-gradient(160deg,var(--photo-warm-1),var(--photo-warm-2) 60%,#4a4644)}
.splash .photo{position:absolute;inset:0;background:radial-gradient(ellipse at 40% 45%,rgba(200,170,150,.45),transparent 60%)}
.splash .brandmark{position:absolute;top:184px;left:0;right:0;font-size:28px}
.splash .brandmark i{width:16px;height:16px}
.splash .ring{position:absolute;left:91px;top:260px}

/* login */
.login{left:354px;top:67px;height:405px;background:linear-gradient(170deg,#6a625d,#4c4846 55%,#6c6560)}
.login .card{position:absolute;left:17px;top:32px;width:200px;height:357px;background:var(--white);border-radius:12px;padding:0 16px}
.login .brandmark{margin-top:46px;font-size:19px;height:30px}
.login .brandmark i{width:11px;height:11px}
.login .label{display:block;margin-top:15px;height:14px}
.login .label.first{margin-top:40px}
.login .pill{margin-top:0}
.login .btn{height:32px;margin-top:22px}
.login .link{text-align:center;font-size:9px;color:var(--ink);text-transform:uppercase;letter-spacing:.3px}
.login .or{position:relative;height:22px;margin:6px 0 4px;display:flex;justify-content:center;align-items:center}
.login .or::before{content:"";position:absolute;left:44px;right:44px;top:11px;height:1px;background:var(--green)}
.login .or span{position:relative;width:22px;height:22px;border-radius:50%;background:var(--green-bright);color:var(--white);font-size:9px;display:flex;align-items:center;justify-content:center}

/* registration */
.register{left:634px;top:67px;height:610px;background:var(--panel-dark)}
.register .card{position:absolute;left:17px;top:78px;width:200px;height:515px;background:var(--white);border-radius:10px;padding:11px 15px 0}
.field{height:44.4px}
.field .label{display:block;line-height:14px}
.field .pill{margin-top:3px}
.upload{position:relative;padding-right:0}
.upload b{position:absolute;right:-1px;top:-1px;height:21px;width:57px;border-radius:11px;background:var(--green);color:var(--white);font-size:8.5px;font-weight:400;display:flex;align-items:center;justify-content:center}
.dob{display:flex;gap:7px;margin-top:3px}
.dob .pill{margin:0;flex:1;padding:0 9px}
.register .btn{height:32px;margin-top:5px}

/* add family */
.family{left:73px;top:473px;height:750px}
.family .segbar{height:48px;background:var(--panel-dark);display:flex;align-items:center;justify-content:center}
.seg{width:208px;height:21px;border-radius:11px;background:var(--white);display:flex;overflow:hidden}
.seg span{flex:1}
.seg .on{flex:0 0 55px;background:var(--green);color:var(--white);font-size:10px;display:flex;align-items:center;justify-content:center;margin-left:84px;flex-grow:0}
.section{position:relative;height:160px;padding:10px 12px 0;border-bottom:1px solid #ececec}
.section h2{text-align:center;font-size:11.5px;font-weight:700;color:var(--green-text);text-transform:uppercase;letter-spacing:.3px;height:18px}
.section .add{position:absolute;right:11px;top:10px;color:var(--green);font-size:15px;line-height:15px}
.section .pill{margin-bottom:8px;height:20px}
.section .row{display:flex;gap:27px;margin-top:3px}
.section .row>div{width:88px}
.section .row .label{display:block;height:14px}
.toggle{width:69px;height:21px;border-radius:11px;background:var(--field);border:1px solid var(--field-line);display:flex;align-items:center;justify-content:space-between;padding-right:7px}
.toggle b{width:38px;height:19px;border-radius:10px;background:var(--green);color:var(--white);font-size:11px;display:flex;align-items:center;justify-content:center}
.pager{display:flex;justify-content:center;gap:5px;margin-top:12px}
.pager i{width:10px;height:10px;border-radius:50%;background:#ededed}
.pager i.on{background:var(--green)}
.section.last{border-bottom:0;height:166px}

/* profile */
.profile{left:374px;top:515px;height:369px}
.profile .portrait{height:107px;background:linear-gradient(90deg,#e6e6e6,#d4d4d4 60%,#9a8378 80%,#d9d9d9)}
.tabsbar{height:47px;background:var(--panel-dark);display:flex;align-items:center;justify-content:center}
.tabs{display:flex;height:21px;border-radius:11px;background:var(--field);overflow:hidden;font-size:9.5px}
.tabs span{display:flex;align-items:center;padding:0 13px;color:var(--ink);border-right:1px solid #ccc}
.tabs span.on{background:var(--green);color:var(--white);border:0;padding:0 12px}
.month{height:48px;display:flex;align-items:center;padding-left:12px;gap:10px;border-bottom:1px solid #eee}
.month .pill{color:var(--ink);font-size:9.5px;padding:0 14px;text-transform:none}
.bday{height:35px;display:flex;align-items:center;font-size:9.5px;color:var(--muted);border-bottom:1px solid #eee;padding-left:12px}
.bday.alt{background:#f6f6f6}
.bday .d{width:14px;text-align:right}
.bday .box{width:18px;height:17px;border:1px solid #ddd;background:#f1f1f1;margin:0 8px 0 9px;font-size:7.5px;display:flex;align-items:center;justify-content:center;color:var(--ink)}
.bday .n{width:78px}
</style>
</head>
<body>
<div class="stage">

  <!-- Splash -->
  <section class="screen splash">
    <div class="photo" role="img" aria-label="Blurred family portrait photograph"></div>
    <div class="status dim">
      <span class="carrier">●●●○○ CELLO <svg width="9" height="7" viewBox="0 0 9 7"><path d="M1 2.5a5 5 0 0 1 7 0M2.5 4a3 3 0 0 1 4 0" stroke="#fff" fill="none"/><circle cx="4.5" cy="5.8" r=".9" fill="#fff"/></svg></span>
      <span class="time">4:21PM</span>
      <span class="batt">20% <svg width="18" height="8" viewBox="0 0 18 8"><rect x=".5" y=".5" width="15" height="7" rx="1" fill="none" stroke="#fff"/><rect x="2" y="2" width="3" height="4" fill="#fff"/><rect x="16" y="2.5" width="1.5" height="3" fill="#fff"/></svg></span>
    </div>
    <div class="brandmark"><i></i>KINROOT</div>
    <svg class="ring" width="50" height="50" viewBox="0 0 50 50">
      <circle cx="25" cy="25" r="21" fill="none" stroke="#fff" stroke-width="5" stroke-dasharray="6 2"/>
      <circle cx="25" cy="25" r="21" fill="none" stroke="#7bd43f" stroke-width="5" stroke-dasharray="6 2 6 2 6 2 6 2 6 2 6 2 6 200" transform="rotate(-90 25 25)" transform-origin="25 25"/>
      <circle cx="25" cy="25" r="17" fill="#333"/>
      <text x="25" y="28.5" text-anchor="middle" font-size="10" fill="#fff" font-family="Source Sans 3, sans-serif">33%</text>
    </svg>
  </section>

  <!-- Login -->
  <section class="screen login">
    <div class="status">
      <span class="carrier">●●●○○ CELLO <svg width="9" height="7" viewBox="0 0 9 7"><path d="M1 2.5a5 5 0 0 1 7 0M2.5 4a3 3 0 0 1 4 0" stroke="#fff" fill="none"/><circle cx="4.5" cy="5.8" r=".9" fill="#fff"/></svg></span>
      <span class="time">4:21PM</span>
      <span class="batt">20% <svg width="18" height="8" viewBox="0 0 18 8"><rect x=".5" y=".5" width="15" height="7" rx="1" fill="none" stroke="#fff"/><rect x="2" y="2" width="3" height="4" fill="#fff"/><rect x="16" y="2.5" width="1.5" height="3" fill="#fff"/></svg></span>
    </div>
    <div class="card">
      <div class="brandmark"><i></i>KINROOT</div>
      <span class="label first">Mobile Number</span>
      <div class="pill"></div>
      <span class="label">Password</span>
      <div class="pill"></div>
      <div class="btn">Login</div>
      <p class="link" style="margin-top:17px">Register</p>
      <div class="or"><span>or</span></div>
      <p class="link">Forgot Password?</p>
    </div>
  </section>

  <!-- Registration -->
  <section class="screen register">
    <div class="status green">
      <span class="carrier">●●●○○ CELLO <svg width="9" height="7" viewBox="0 0 9 7"><path d="M1 2.5a5 5 0 0 1 7 0M2.5 4a3 3 0 0 1 4 0" stroke="#fff" fill="none"/><circle cx="4.5" cy="5.8" r=".9" fill="#fff"/></svg></span>
      <span class="time">4:21PM</span>
      <span class="batt">20% <svg width="18" height="8" viewBox="0 0 18 8"><rect x=".5" y=".5" width="15" height="7" rx="1" fill="none" stroke="#fff"/><rect x="2" y="2" width="3" height="4" fill="#fff"/><rect x="16" y="2.5" width="1.5" height="3" fill="#fff"/></svg></span>
    </div>
    <header class="appbar">
      <svg width="13" height="11" viewBox="0 0 13 11"><path d="M0 1h13M0 5.5h13M0 10h13" stroke="#fff" stroke-width="1.6"/></svg>
      <h1>New Registration</h1>
      <svg width="13" height="13" viewBox="0 0 13 13"><circle cx="5" cy="5" r="3.8" fill="none" stroke="#fff" stroke-width="2"/><path d="M8 8l4 4" stroke="#fff" stroke-width="2.4" stroke-linecap="round"/></svg>
    </header>
    <div class="card">
      <div class="field"><span class="label">Profile Picture</span><div class="pill upload"><b>BROWS</b></div></div>
      <div class="field"><span class="label">First Name</span><div class="pill">Kevin</div></div>
      <div class="field"><span class="label">Last Name</span><div class="pill">Smith</div></div>
      <div class="field"><span class="label">Date of Birth</span>
        <div class="dob"><div class="pill select">1</div><div class="pill select">Jan</div><div class="pill select">1985</div></div></div>
      <div class="field"><span class="label">Gender</span><div class="pill select">Male</div></div>
      <div class="field"><span class="label">Password</span><div class="pill">**********</div></div>
      <div class="field"><span class="label">Email Address</span><div class="pill">ab@example.com</div></div>
      <div class="field"><span class="label">Country</span><div class="pill select">India</div></div>
      <div class="field"><span class="label">Current City</span><div class="pill">New Delhi</div></div>
      <div class="field"><span class="label">Mobile Number</span><div class="pill">+91-900123XXXX</div></div>
      <div class="btn">Register Now</div>
    </div>
  </section>

  <!-- Add family -->
  <section class="screen family">
    <div class="status green">
      <span class="carrier">●●●○○ CELLO <svg width="9" height="7" viewBox="0 0 9 7"><path d="M1 2.5a5 5 0 0 1 7 0M2.5 4a3 3 0 0 1 4 0" stroke="#fff" fill="none"/><circle cx="4.5" cy="5.8" r=".9" fill="#fff"/></svg></span>
      <span class="time">4:21PM</span>
      <span class="batt">20% <svg width="18" height="8" viewBox="0 0 18 8"><rect x=".5" y=".5" width="15" height="7" rx="1" fill="none" stroke="#fff"/><rect x="2" y="2" width="3" height="4" fill="#fff"/><rect x="16" y="2.5" width="1.5" height="3" fill="#fff"/></svg></span>
    </div>
    <header class="appbar">
      <svg width="13" height="11" viewBox="0 0 13 11"><path d="M0 1h13M0 5.5h13M0 10h13" stroke="#fff" stroke-width="1.6"/></svg>
      <h1>Add Family</h1>
      <svg width="13" height="13" viewBox="0 0 13 13"><circle cx="5" cy="5" r="3.8" fill="none" stroke="#fff" stroke-width="2"/><path d="M8 8l4 4" stroke="#fff" stroke-width="2.4" stroke-linecap="round"/></svg>
    </header>
    <div class="segbar"><div class="seg"><span class="on">Family</span></div></div>

    <div class="section">
      <h2>Parents</h2><span class="add">+</span>
      <div class="pill"></div><div class="pill"></div>
      <div class="row"><div><span class="label">Gender</span><div class="pill select">Male</div></div>
        <div><span class="label">Alive</span><div class="toggle"><b>X</b><svg width="10" height="8" viewBox="0 0 10 8"><path d="M1 4l3 3 5-6" stroke="#888" fill="none" stroke-width="1.3"/></svg></div></div></div>
      <div class="pager"><i class="on"></i><i></i><i></i></div>
    </div>
    <div class="section">
      <h2>Spouse</h2><span class="add">+</span>
      <div class="pill"></div><div class="pill"></div>
      <div class="row"><div><span class="label">Gender</span><div class="pill select">Male</div></div>
        <div><span class="label">Alive</span><div class="toggle"><b>X</b><svg width="10" height="8" viewBox="0 0 10 8"><path d="M1 4l3 3 5-6" stroke="#888" fill="none" stroke-width="1.3"/></svg></div></div></div>
      <div class="pager"><i></i><i></i><i class="on"></i><i></i><i></i></div>
    </div>
    <div class="section">
      <h2>Siblings</h2><span class="add">+</span>
      <div class="pill"></div><div class="pill"></div>
      <div class="row"><div><span class="label">Gender</span><div class="pill select">Male</div></div>
        <div><span class="label">Alive</span><div class="toggle"><b>X</b><svg width="10" height="8" viewBox="0 0 10 8"><path d="M1 4l3 3 5-6" stroke="#888" fill="none" stroke-width="1.3"/></svg></div></div></div>
      <div class="pager"><i class="on"></i><i></i></div>
    </div>
    <div class="section last">
      <h2>Children</h2><span class="add">+</span>
      <div class="pill"></div><div class="pill"></div>
      <div class="row"><div><span class="label">Gender</span><div class="pill select">Male</div></div>
        <div><span class="label">Alive</span><div class="toggle"><b>X</b><svg width="10" height="8" viewBox="0 0 10 8"><path d="M1 4l3 3 5-6" stroke="#888" fill="none" stroke-width="1.3"/></svg></div></div></div>
      <div class="pager"><i></i><i class="on"></i><i></i></div>
    </div>
  </section>

  <!-- Profile / birthdays -->
  <section class="screen profile">
    <div class="status green">
      <span class="carrier">●●●○○ CELLO <svg width="9" height="7" viewBox="0 0 9 7"><path d="M1 2.5a5 5 0 0 1 7 0M2.5 4a3 3 0 0 1 4 0" stroke="#fff" fill="none"/><circle cx="4.5" cy="5.8" r=".9" fill="#fff"/></svg></span>
      <span class="time">4:21PM</span>
      <span class="batt">20% <svg width="18" height="8" viewBox="0 0 18 8"><rect x=".5" y=".5" width="15" height="7" rx="1" fill="none" stroke="#fff"/><rect x="2" y="2" width="3" height="4" fill="#fff"/><rect x="16" y="2.5" width="1.5" height="3" fill="#fff"/></svg></span>
    </div>
    <header class="appbar">
      <svg width="13" height="11" viewBox="0 0 13 11"><path d="M0 1h13M0 5.5h13M0 10h13" stroke="#fff" stroke-width="1.6"/></svg>
      <h1>Kevin Smith</h1>
      <svg width="13" height="13" viewBox="0 0 13 13"><circle cx="5" cy="5" r="3.8" fill="none" stroke="#fff" stroke-width="2"/><path d="M8 8l4 4" stroke="#fff" stroke-width="2.4" stroke-linecap="round"/></svg>
    </header>
    <div class="portrait" role="img" aria-label="Profile photograph of the user"></div>
    <div class="tabsbar"><div class="tabs"><span>Notifications</span><span>Photos</span><span class="on">Birthdays</span></div></div>
    <div class="month">
      <svg width="9" height="13" viewBox="0 0 9 13"><path d="M7.5 1L2 6.5 7.5 12" stroke="#7bd43f" stroke-width="1.8" fill="none"/></svg>
      <div class="pill">January</div>
    </div>
    <div class="bday alt"><span class="d">9</span><span class="box">8</span><span class="n">Jan Doe</span><span>31 Years</span></div>
    <div class="bday"><span class="d">18</span><span class="box"></span><span class="n">Jan Doe</span><span>31 Years</span></div>
    <div class="bday"><span class="d">31</span><span class="box"></span><span class="n">Jan Doe</span><span>31 Years</span></div>
  </section>

</div>
</body>
</html>
```